wedding DJ & Lighting entertainment

We are a DJ and Lighting production company. We specialize mainly in wedding entertainment. I've attached my old postcard in the image folder, however, i would like something new and updated. You can use the same bullet points from the front page, but i would like to have a cleaner look on the front. I'd like to have one large image on the front side and smaller images on the back side. I'd also like to have some text below the logo. I'd like it to say DJ * Lighting * Audio/Visual. I'd also like to have the phrase "Celebrate with Style"

Target Market(s)

weddings, private events, women

Industry/Entity Type

It Company

Font styles to use
Sans Serif
Script

Requirements
Must have
• look elegant, sophisticated. Must have my new logo! My logo is attached as one of the files. It's a headphone logo.

```html
<!DOCTYPE html>
<html lang="en">
<head>
<meta charset="utf-8">
<title>Lumenbeat Events – Postcard</title>
<link rel="stylesheet" href="https://fonts.googleapis.com/css2?family=Quicksand:wght@500&family=Open+Sans:wght@400;600&family=Great+Vibes&display=swap">
<style>
  :root {
    --canvas-bg: #ecebef;
    --card-top: #fbf9fd;
    --card-lilac: #e6d8f2;
    --card-pink: #f6dcea;
    --frame: #ffffff;
    --swoosh: #d4166e;
    --swoosh-deep: #b0104e;
    --brand-red: #e2262b;
    --ink: #222222;
    --ink-soft: #333333;
    --ink-muted: #666666;
  }
  * { box-sizing: border-box; margin: 0; padding: 0; }
  html, body { width: 800px; height: 1200px; overflow: hidden; }
  body { background: var(--canvas-bg); position: relative; }

  .postcard {
    position: absolute; left: 20px; top: 305px;
    width: 760px; height: 589px;
    background: linear-gradient(120deg, var(--card-top) 0%, var(--card-top) 35%, var(--card-lilac) 70%, var(--card-pink) 100%);
    box-shadow: 0 4px 14px rgba(0,0,0,.25);
    overflow: hidden;
  }
  .photo {
    position: absolute;
    border: 3px solid var(--frame);
    box-shadow: 0 1px 4px rgba(0,0,0,.3);
  }
  .photo--table    { left: 25px;  top: 25px;  width: 194px; height: 170px; background: linear-gradient(160deg, #3a2c8c, #6a56c8 55%, #d8cfe8); }
  .photo--ballroom { left: 233px; top: 25px;  width: 283px; height: 170px; background: linear-gradient(180deg, #2c2f86, #4b52c0 45%, #7b78c8 75%, #b6a46a); }
  .photo--crowd-bw { left: 530px; top: 25px;  width: 204px; height: 170px; background: linear-gradient(150deg, #e8e8e8, #6b6b6b 50%, #1c1c1c); }
  .photo--first-dance { left: 25px; top: 210px; width: 491px; height: 174px; background: linear-gradient(90deg, #2a1c3c, #5a3a70 45%, #c6b47a 75%, #3c2a4e); }
  .photo--pink-party  { left: 530px; top: 210px; width: 204px; height: 174px; background: linear-gradient(180deg, #e8308e, #b83474 45%, #6a3a4a); }
  .photo--circle-dance { left: 233px; top: 402px; width: 283px; height: 161px; background: linear-gradient(170deg, #1e1a2a, #6a4a5a 45%, #b88a6a 80%, #ece4e0); }
  .photo--party-bw     { left: 530px; top: 402px; width: 204px; height: 161px; background: linear-gradient(160deg, #1a1a1a, #707070 55%, #cfcfcf); }

  .swoosh { position: absolute; left: 0; top: 0; width: 760px; height: 589px; }

  .tagline {
    position: absolute; left: 34px; top: 432px;
    font-family: "Great Vibes", cursive; font-size: 24px; color: var(--swoosh);
    white-space: nowrap;
  }
  .brand {
    position: absolute; left: 36px; top: 470px;
    display: flex; align-items: center; gap: 8px;
  }
  .brand__dot { width: 12px; height: 12px; border-radius: 50%; background: var(--brand-red); }
  .brand__name {
    font-family: "Quicksand", sans-serif; font-weight: 500;
    font-size: 26px; color: var(--brand-red); white-space: nowrap;
  }
  .services {
    position: absolute; left: 38px; top: 508px;
    font-family: "Open Sans", sans-serif; font-weight: 600;
    font-size: 9px; letter-spacing: 1.8px; color: var(--ink-muted);
    white-space: nowrap;
  }
  .phone {
    position: absolute; left: 36px; top: 536px;
    display: flex; align-items: center; gap: 8px;
    font-family: "Open Sans", sans-serif; font-size: 19px; color: var(--ink);
    white-space: nowrap;
  }
  .contact {
    position: absolute; left: 240px; top: 540px;
    font-family: "Open Sans", sans-serif; font-size: 10.5px; color: var(--ink-soft);
    line-height: 16px;
  }
  .contact__row { display: flex; align-items: center; gap: 5px; }
</style>
</head>
<body>
  <section class="postcard">
    <div class="photo photo--table" role="img" aria-label="Reception table with centrepiece under purple uplighting"></div>
    <div class="photo photo--ballroom" role="img" aria-label="Ballroom with blue uplighting, wedding cake and monogram projected on the dance floor"></div>
    <div class="photo photo--crowd-bw" role="img" aria-label="Black and white photo of guests dancing with raised hands"></div>
    <div class="photo photo--first-dance" role="img" aria-label="Large photo of the bride and groom sharing their first dance in a lit reception hall"></div>
    <div class="photo photo--pink-party" role="img" aria-label="Guests dancing under pink lighting"></div>
    <div class="photo photo--circle-dance" role="img" aria-label="Bride dancing with guests in a circle on the dance floor"></div>
    <div class="photo photo--party-bw" role="img" aria-label="Black and white photo of a crowd dancing at a reception"></div>

    <svg class="swoosh" viewBox="0 0 760 589" aria-hidden="true">
      <path d="M0 103 C40 300 200 480 655 589 L0 589 Z" fill="#ffffff" fill-opacity="0.9"/>
      <path d="M0 103 C40 300 200 480 655 589" fill="none" stroke="var(--swoosh)" stroke-width="5"/>
      <path d="M0 111 C44 305 205 486 635 589" fill="none" stroke="var(--swoosh-deep)" stroke-width="1.5" stroke-opacity=".6"/>
    </svg>

    <div class="tagline">Celebrate with Style</div>

    <div class="brand">
      <span class="brand__dot"></span>
      <span class="brand__name">lumenbeat events</span>
    </div>

    <div class="services">DJ • LIGHTING • AUDIO/VISUAL</div>

    <div class="phone">
      <svg width="16" height="16" viewBox="0 0 24 24" aria-hidden="true">
        <path d="M6.6 10.8a15.1 15.1 0 0 0 6.6 6.6l2.2-2.2a1 1 0 0 1 1-.25 11.4 11.4 0 0 0 3.6.57 1 1 0 0 1 1 1V20a1 1 0 0 1-1 1A17 17 0 0 1 3 4a1 1 0 0 1 1-1h3.5a1 1 0 0 1 1 1 11.4 11.4 0 0 0 .57 3.6 1 1 0 0 1-.25 1z" fill="none" stroke="var(--ink)" stroke-width="2"/>
      </svg>
      <span>555-201-4470</span>
    </div>

    <div class="contact">
      <div class="contact__row">
        <svg width="8" height="8" viewBox="0 0 10 10" aria-hidden="true"><circle cx="5" cy="5" r="4" fill="none" stroke="var(--ink-soft)" stroke-width="1.4"/></svg>
        <span>lumenbeatevents.com</span>
      </div>
      <div class="contact__row">
        <svg width="8" height="7" viewBox="0 0 10 8" aria-hidden="true"><rect x="0" y="0" width="10" height="8" fill="var(--ink-soft)"/><path d="M0 0 L5 4.5 L10 0" fill="none" stroke="#fff" stroke-width="1"/></svg>
        <span>hello@lumenbeatevents.com</span>
      </div>
    </div>
  </section>
</body>
</html>
```